Banner dimension 1767 X 887 for Tovarelo website

Need one banner for our website www.tovarelo.com.au, The dimension of the banner should be 1767 x 887. Attached to this brief are two images that needs to be on that one banner, PLEASE DO NOT SEND SEPARATE BANNERS, both images on the same banner. Thanks

The banner should have the following message on it:

1.) " Take a further 40% off all stock" ( use code: TOVARELO. Ends 31/12/2015)
2.) " Kick back or kick it up a notch this Autumn in the most versatile pique striped polo shirts and Pinafore belt strap denim dress"

Target Market(s)

kids aged 5-12yrs

Requirements
Must have
• very playful

```html
<!DOCTYPE html>
<html lang="en">
<head>
<meta charset="utf-8">
<title>Tovarelo – Autumn Kids Banner</title>
<link rel="stylesheet" href="https://fonts.googleapis.com/css2?family=Architects+Daughter&family=Fira+Sans:wght@400;600;700&display=swap">
<style>
  :root {
    --paper: #ffffff;
    --slate: #3b5567;
    --slate-text: #2f4a5c;
    --forest: #4d6b5b;
    --promo-red: #b8141b;
    --ink-light: #f3f5f2;
    --photo-boy-a: #d9d4cc;
    --photo-boy-b: #4f7a5a;
    --photo-girl-a: #e9e4df;
    --photo-girl-b: #52789c;
  }
  * { margin: 0; padding: 0; box-sizing: border-box; }
  html, body { width: 1200px; height: 602px; overflow: hidden; background: var(--paper); }
  .banner {
    position: relative;
    width: 1200px;
    height: 602px;
    background: var(--paper);
    font-family: "Fira Sans", Arial, sans-serif;
    overflow: hidden;
  }
  .hand {
    font-family: "Architects Daughter", "Comic Sans MS", cursive;
    text-transform: uppercase;
    white-space: nowrap;
  }
  .promo-code {
    position: absolute; left: 30px; top: 14px;
    color: var(--slate-text); font-size: 17px; white-space: nowrap;
  }
  .promo-code .code { font-size: 27px; font-weight: 700; letter-spacing: 0.5px; margin: 0 3px; }
  .promo-code .ends { font-size: 16px; }
  .promo-offer {
    position: absolute; left: 28px; top: 58px;
    color: var(--promo-red); font-size: 20px; font-weight: 600; white-space: nowrap;
  }
  .promo-offer .percent { font-size: 40px; font-weight: 700; margin: 0 2px; }
  .brush-stroke { position: absolute; left: 430px; top: 18px; width: 440px; height: 224px; }
  .headline {
    position: absolute; left: 506px; top: 78px;
    color: var(--ink-light); font-size: 38px; line-height: 44px; font-weight: 400;
    letter-spacing: 3px;
    transform: rotate(-3deg); transform-origin: left top;
  }
  .tag {
    position: absolute;
    background: var(--forest); color: var(--ink-light);
    font-size: 25px; letter-spacing: 2px;
    display: flex; align-items: center; justify-content: center;
  }
  .tag-versatile { left: 363px; top: 282px; width: 409px; height: 50px; }
  .tag-polo { left: 302px; top: 330px; width: 483px; height: 57px; }
  .dress-line {
    position: absolute; left: 440px; top: 452px; width: 455px;
    color: var(--forest); font-size: 25px; line-height: 42px;
    letter-spacing: 3px; text-align: center;
    transform: rotate(-4deg); transform-origin: center center;
  }
  .photo { position: absolute; }
  .photo-boy {
    left: 18px; top: 120px; width: 300px; height: 470px;
    border-radius: 45% 45% 25% 25%;
    background: linear-gradient(180deg, var(--photo-boy-a) 0%, var(--photo-boy-b) 45%, #9fb4c4 75%, #e8e8e8 100%);
    opacity: 0.5;
  }
  .photo-girl {
    left: 935px; top: 28px; width: 215px; height: 552px;
    border-radius: 48% 48% 20% 20%;
    background: linear-gradient(180deg, var(--photo-girl-a) 0%, var(--photo-girl-b) 40%, #5c7f9f 70%, #e6a3b5 100%);
    opacity: 0.5;
  }
</style>
</head>
<body>
<main class="banner">
  <p class="promo-code">use code: <span class="code">TOVARELO</span> <span class="ends">Ends 31/12/2015</span></p>
  <p class="promo-offer">FURTHER <span class="percent">40% OFF</span> ALL STOCK</p>

  <svg class="brush-stroke" viewBox="0 0 440 224" aria-hidden="true">
    <path fill="var(--slate)" d="M48 12 L430 2 L418 30 L436 56 L404 76 L424 104 L388 126 L420 144 L372 166 L250 176 L132 186 L70 214 L24 204 L44 182 L14 166 L34 138 L8 108 L40 80 L16 52 L30 30 Z"/>
  </svg>
  <h1 class="headline hand">Kick back<br>a notch this</h1>

  <p class="tag tag-versatile hand">In the most versatile</p>
  <p class="tag tag-polo hand">Pique striped polo shirts</p>

  <p class="dress-line hand">And pinafore belt strap<br>denim dress!</p>

  <div class="photo photo-boy" role="img" aria-label="Photo of a smiling boy posing playfully in a green and black striped polo shirt and denim shorts"></div>
  <div class="photo photo-girl" role="img" aria-label="Photo of a smiling girl wearing a white t-shirt under a denim pinafore dress with pink sneakers"></div>
</main>
</body>
</html>
```